full stationary design for a modern sleek design company

we are a design company that does modern minimalistic interior design works as well as other design services for high end clients.
we need a full stationary design including and not limited to (double sided business card, letter head, envelopes, documents folder...etc) that reflects the modern style design we do.
sleek modern and minimalistic is the requirements.
Updates

please use the latest attached files as there was a slight modification on the logo Added Wednesday, March 1, 2017

minor update on the logo files in JPG and PSD has been updated kindly follow the new attachments. Added Thursday, March 2, 2017

Target Market(s)

modern minimalist clients

Industry/Entity Type

Design Agency

Requirements
Must have
• the logo
Nice to have
• i like the colors in the colored 3D logo attached
Should not have
• too many colors

```html
<!DOCTYPE html>
<html lang="en">
<head>
<meta charset="utf-8">
<title>Linea Atelier — Stationery Set</title>
<link rel="stylesheet" href="https://fonts.googleapis.com/css2?family=Montserrat:wght@500;600&family=Arimo:wght@400&display=swap">
<style>
:root{
  --navy:#2b3242;
  --copper:#b8673f;
  --slate:#8f8f8f;
  --slate-dark:#7d7d7d;
  --ghost-grey:#d6d6d8;
  --ghost-copper:#f1ddd2;
  --paper:#ffffff;
  --ink:#3a3a3a;
  --backdrop:#e8eaea;
}
*{box-sizing:border-box;margin:0;padding:0}
html,body{width:1200px;height:900px;overflow:hidden;background:var(--backdrop)}
body{position:relative;font-family:"Arimo",Arial,sans-serif;color:var(--ink)}
.sheet{position:absolute;background:var(--paper);box-shadow:0 3px 10px rgba(0,0,0,.12);overflow:hidden}
.bands{position:absolute;left:0;bottom:0;width:100%}
.brand{display:flex;align-items:center;gap:6px;font-family:"Montserrat",sans-serif;font-weight:600;color:var(--navy);letter-spacing:.06em;text-transform:uppercase;white-space:nowrap}
.brand .mark{width:10px;height:10px;background:var(--copper);flex:none}
.brand-tag{font-family:"Montserrat",sans-serif;font-weight:600;color:var(--navy);letter-spacing:.25em;text-transform:uppercase;font-size:6px;margin-top:2px}
.ghost-name{position:absolute;font-family:"Montserrat",sans-serif;font-weight:600;line-height:1;white-space:nowrap}
.icon{width:9px;height:9px;flex:none}
.contact{display:flex;align-items:center;gap:5px;font-size:7px;color:var(--ink)}

/* letterhead */
.letterhead{left:40px;top:40px;width:380px;height:537px}
.letterhead .rule-top{position:absolute;left:24px;right:120px;top:34px;height:1px;background:var(--navy)}
.letterhead .rule-right{position:absolute;left:250px;right:22px;top:78px;height:1px;background:var(--copper)}
.letterhead .brand-block{position:absolute;right:22px;top:26px;font-size:10px}
.letterhead .ghost-name{left:60px;top:250px;font-size:130px;color:var(--ghost-copper);opacity:.7}
.letterhead .salutation{position:absolute;left:26px;top:70px;font-size:8px}
.letterhead .recipient{position:absolute;right:26px;top:96px;font-size:7px;text-align:right;line-height:1.35}
.letterhead .body{position:absolute;left:26px;right:26px;top:160px;font-size:6.6px;line-height:1.55;text-align:justify}
.letterhead .body p{margin-bottom:8px}
.letterhead .signoff{position:absolute;left:26px;top:385px;font-size:7px;color:#777}
.letterhead .footer-web{position:absolute;left:26px;top:468px;display:flex;flex-direction:column;gap:8px}
.letterhead .footer-web .contact{font-size:6px;color:var(--copper)}
.letterhead .footer-rule{position:absolute;left:22px;width:160px;top:463px;height:1px;background:var(--navy)}
.letterhead .footer-phone{position:absolute;left:212px;top:478px;display:flex;flex-direction:column;gap:6px}
.letterhead .footer-phone .contact{font-size:6px}

/* folder */
.folder{left:440px;top:40px;width:380px;height:537px;background:var(--slate)}
.folder .ghost-name{left:40px;top:170px;font-size:150px;color:var(--slate-dark)}
.folder .tab-navy{position:absolute;right:0;top:300px;width:10px;height:70px;background:var(--navy)}
.folder .tab-copper{position:absolute;right:0;top:380px;width:10px;height:70px;background:var(--copper)}
.folder .brand{position:absolute;right:26px;bottom:40px;font-size:11px;color:var(--navy)}

/* business cards */
.card{width:320px;height:182px}
.card-front{left:840px;top:40px}
.card-back{left:840px;top:250px;background:var(--slate)}
.card-front .ghost-name{left:150px;top:18px;font-size:70px;color:var(--ghost-grey)}
.card-front .brand-block{position:absolute;left:150px;top:68px;font-size:9px}
.card-front .rule{position:absolute;left:18px;top:40px;width:110px;height:1px;background:var(--navy)}
.card-front .web{position:absolute;left:18px;top:48px;display:flex;flex-direction:column;gap:7px}
.card-front .web .contact{font-size:6.5px;color:var(--copper)}
.card-front .details{position:absolute;left:150px;top:106px;display:flex;flex-direction:column;gap:6px}
.card-front .details .contact{font-size:6.5px}
.card-back .ghost-name{left:16px;top:10px;font-size:80px;color:var(--slate-dark)}
.card-back .strip{position:absolute;left:0;right:0;top:74px;height:44px;background:var(--paper);display:flex;flex-direction:column;justify-content:center;padding-left:22px}
.card-back .strip .brand{font-size:11px}

/* envelope */
.envelope{left:330px;top:615px;width:540px;height:255px}
.envelope .flap{position:absolute;inset:0;width:100%;height:100%}
.envelope .brand-block{position:absolute;left:26px;top:30px;font-size:12px}
.envelope .brand-block .brand-tag{font-size:7px}
.envelope .details{position:absolute;left:26px;top:84px;display:flex;flex-direction:column;gap:9px}
.envelope .ghost-name{left:250px;top:90px;font-size:110px;color:var(--ghost-copper)}
</style>
</head>
<body>

<!-- Letterhead -->
<section class="sheet letterhead" aria-label="Letterhead">
  <div class="ghost-name" aria-hidden="true">Linea</div>
  <div class="rule-top"></div>
  <div class="brand-block">
    <div class="brand"><span class="mark"></span>Linea Atelier</div>
    <div class="brand-tag">by Marc Devaux</div>
  </div>
  <div class="rule-right"></div>
  <p class="salutation">Dear Mr. Hartley</p>
  <address class="recipient" style="font-style:normal">
    Owen Hartley<br>BrightNest<br>Suite 7, 18 Orchard Lane<br>Westbrook 4120<br>Freeland
  </address>
  <div class="body">
    <p>Lorem ipsum dolor sit amet, consectetur adipiscing elit. Vestibulum adipiscing felis ac tortor consectetur feugiat. Etiam malesuada sodales eros ut ornare. Sed lorem eros, mattis id pretium ut, faucibus sit amet quam. Nullam consectetur ultrices ipsum, fringilla porttitor erat ornare at. Sed sit amet dui vel sapien ultrices vulputate. In hac habitasse platea dictumst. Nam est nisi, rhoncus et sagittis a, porttitor adipiscing nulla. Vivamus placerat felis ultrices quam iaculis eget dignissim felis egestas. Integer nec molestie lorem. Sed odio tellus, vulputate sed laoreet non, vulputate id justo. Etiam suscipit, odio vel auctor dictum, felis turpis ullamcorper neque, quis sodales risus metus in magna. Morbi pellentesque justo et quam laoreet facilisis. Aenean placerat, urna ornare aliquet tincidunt, lorem justo molestie ligula, id placerat eros semper sit amet faucibus sit amet.</p>
    <p>Aenean ut congue tellus. Class aptent taciti sociosqu ad litora torquent per conubia nostra, per inceptos himenaeos. Sed facilisis, velit tincidunt pharetra fermentum, urna tortor iaculis erat, vitae sollicitudin leo mauris quis mi. Cras malesuada sem ac ipsum sagittis ultrices. Mauris fermentum porttitor nisi, eu facilisis lorem consectetur at. Suspendisse vel elit, scelerisque ac euismod id, scelerisque viverra odio. Nullam scelerisque metus in eros semper congue. Fusce a fermentum est. Ut ac leo dolor. Quisque dignissim mauris a neque luctus pretium ultrices risus sagittis. Aenean quam massa, rutrum ac hendrerit eu, interdum eu nulla. Curabitur a velit mauris, sed porta eros. Cras et egestas sapien. Proin non metus eget felis eleifend adipiscing. Nunc malesuada pharetra blandit.</p>
  </div>
  <p class="signoff">Your sincerely</p>

  <div class="footer-rule"></div>
  <div class="footer-web">
    <span class="contact"><svg class="icon" viewBox="0 0 10 10"><circle cx="5" cy="5" r="4" fill="none" stroke="currentColor"/><path d="M1 5h8M5 1c2 2 2 6 0 8M5 1c-2 2-2 6 0 8" fill="none" stroke="currentColor" stroke-width=".7"/></svg>www.yoursite.com</span>
    <span class="contact"><svg class="icon" viewBox="0 0 10 10"><rect x=".5" y="2" width="9" height="6" fill="none" stroke="currentColor"/><path d="M.5 2l4.5 3.5L9.5 2" fill="none" stroke="currentColor"/></svg>yourmail@email.com</span>
  </div>
  <div class="footer-phone">
    <span class="contact"><svg class="icon" viewBox="0 0 10 10"><path d="M2 1h2l1 2.5-1.3 1a6 6 0 0 0 2.8 2.8l1-1.3L10 7v2c-5 .5-9-3.5-8.5-8z" fill="var(--navy)"/></svg>(01) 555 010 220</span>
    <span class="contact"><svg class="icon" viewBox="0 0 10 10"><path d="M5 .5L.5 5H2v4.5h2.3V6.5h1.4v3H8V5h1.5z" fill="var(--navy)"/></svg>Your Street Name 123 · 555777 UAE</span>
  </div>
  <svg class="bands" viewBox="0 0 380 70" height="70" preserveAspectRatio="none" aria-hidden="true">
    <polygon points="0,0 185,0 200,16 0,16" fill="var(--navy)"/>
    <polygon points="190,0 205,0 220,60 380,60 380,70 200,70" fill="var(--copper)"/>
    <rect x="205" y="0" width="175" height="1" fill="var(--copper)"/>
    <rect x="205" y="56" width="175" height="14" fill="var(--copper)"/>
  </svg>
</section>

<!-- Document folder -->
<section class="sheet folder" aria-label="Document folder">
  <div class="ghost-name" aria-hidden="true">Linea</div>
  <div class="tab-navy"></div>
  <div class="tab-copper"></div>
  <div class="brand"><span class="mark"></span>Linea Atelier</div>
  <svg class="bands" viewBox="0 0 380 30" height="30" preserveAspectRatio="none" aria-hidden="true">
    <polygon points="0,0 180,0 195,14 0,14" fill="var(--navy)"/>
    <polygon points="190,0 200,0 215,18 380,18 380,30 205,30" fill="var(--copper)"/>
  </svg>
</section>

<!-- Business card front -->
<section class="sheet card card-front" aria-label="Business card, front">
  <div class="ghost-name" aria-hidden="true">Linea</div>
  <div class="rule"></div>
  <div class="web">
    <span class="contact"><svg class="icon" viewBox="0 0 10 10"><circle cx="5" cy="5" r="4" fill="none" stroke="currentColor"/><path d="M1 5h8" stroke="currentColor"/></svg>www.yoursite.com</span>
    <span class="contact"><svg class="icon" viewBox="0 0 10 10"><rect x=".5" y="2" width="9" height="6" fill="none" stroke="currentColor"/><path d="M.5 2l4.5 3.5L9.5 2" fill="none" stroke="currentColor"/></svg>yourmail@email.com</span>
  </div>
  <div class="brand-block">
    <div class="brand"><span class="mark"></span>Linea Atelier</div>
    <div class="brand-tag">by Marc Devaux</div>
  </div>
  <div class="details">
    <span class="contact"><svg class="icon" viewBox="0 0 10 10"><path d="M2 1h2l1 2.5-1.3 1a6 6 0 0 0 2.8 2.8l1-1.3L10 7v2c-5 .5-9-3.5-8.5-8z" fill="var(--navy)"/></svg>(01) 555 010 220</span>
    <span class="contact"><svg class="icon" viewBox="0 0 10 10"><path d="M5 .5L.5 5H2v4.5h2.3V6.5h1.4v3H8V5h1.5z" fill="var(--navy)"/></svg>Your Street Name 123 · 555777 UAE</span>
  </div>
  <svg class="bands" viewBox="0 0 320 34" height="34" preserveAspectRatio="none" aria-hidden="true">
    <polygon points="0,0 120,0 132,12 0,12" fill="var(--navy)"/>
    <polygon points="130,0 138,0 150,22 320,22 320,34 142,34" fill="var(--copper)"/>
  </svg>
</section>

<!-- Business card back -->
<section class="sheet card card-back" aria-label="Business card, back">
  <div class="ghost-name" aria-hidden="true">Linea</div>
  <div class="strip">
    <div class="brand"><span class="mark"></span>Linea Atelier</div>
    <div class="brand-tag">by Marc Devaux</div>
  </div>
  <svg class="bands" viewBox="0 0 320 40" height="40" preserveAspectRatio="none" aria-hidden="true">
    <polygon points="0,0 130,0 140,40 0,40" fill="var(--navy)"/>
    <polygon points="140,12 320,12 320,40 148,40" fill="var(--copper)"/>
  </svg>
</section>

<!-- Envelope -->
<section class="sheet envelope" aria-label="Envelope">
  <svg class="flap" viewBox="0 0 540 255" preserveAspectRatio="none" aria-hidden="true">
    <polyline points="150,0 180,22 540,22" fill="none" stroke="#9a9a9a" stroke-width=".7"/>
  </svg>
  <div class="ghost-name" aria-hidden="true">Linea</div>
  <div class="brand-block">
    <div class="brand"><span class="mark"></span>Linea Atelier</div>
    <div class="brand-tag">by Marc Devaux</div>
  </div>
  <div class="details">
    <span class="contact"><svg class="icon" viewBox="0 0 10 10"><path d="M2 1h2l1 2.5-1.3 1a6 6 0 0 0 2.8 2.8l1-1.3L10 7v2c-5 .5-9-3.5-8.5-8z" fill="var(--navy)"/></svg>(01) 555 010 220</span>
    <span class="contact"><svg class="icon" viewBox="0 0 10 10"><path d="M5 .5L.5 5H2v4.5h2.3V6.5h1.4v3H8V5h1.5z" fill="var(--navy)"/></svg>Your Street Name 123 · 555777 UAE</span>
  </div>
  <svg class="bands" viewBox="0 0 540 50" height="50" preserveAspectRatio="none" aria-hidden="true">
    <polygon points="0,0 210,0 225,18 0,18" fill="var(--navy)"/>
    <polygon points="220,0 232,0 250,32 540,32 540,50 240,50" fill="var(--copper)"/>
  </svg>
</section>

</body>
</html>
```